Email Banner for Technology Company

We need a new email banner. The purpose of the email banner is to make us look more professional as a business and keep all communications with clients uniform. The previous designs which we have included below have now become outdated as our brand has developed and we need the new banner to become more aligned and modern.
We are a marketing organization that specialises in lead generation, email newsletters are sent to prospects on a regular basis. Therefore, it is important that we have an aesthetically pleasing banner as this is the first real impression prospects have our business. First impressions matter.
We are looking for a new email banner design as the current design is now outdated and does not reflect who we are as a business.
The new banners are required for launch at the start of Q2.
There is future work in the pipeline for the winning design. We have multiple industry sites that will require the new design as well as creating each of these in multiple languages.
The design must include the Brightwave Briefings wording the tagline 'The Systems Expert’s Insight Desk'.
It needs to be creative and fun but still remain professional, sticking with the colour theme that already exists.

```html
<!DOCTYPE html>
<html lang="en">
<head>
<meta charset="UTF-8">
<title>Brightwave Briefings – Email Banner</title>
<link href="https://fonts.googleapis.com/css2?family=Montserrat:wght@600;700&display=swap" rel="stylesheet">
<style>
  :root {
    --page-bg: #e6e6e6;
    --blue-deep: #0a4fd6;
    --blue-mid: #0f6fe3;
    --blue-light: #1a8ef0;
    --band-tint: rgba(255, 255, 255, 0.06);
    --band-accent: #0a8be6;
    --panel-white: #fdfefb;
    --ink: #0b0b0b;
    --logo-white: #ffffff;
  }
  * { margin: 0; padding: 0; box-sizing: border-box; }
  html, body {
    width: 1200px;
    height: 701px;
    overflow: hidden;
    background: var(--page-bg);
  }
  .canvas {
    position: relative;
    width: 1200px;
    height: 701px;
  }
  .banner {
    position: absolute;
    left: 80px;
    top: 156px;
    width: 1040px;
    height: 390px;
    overflow: hidden;
    background: linear-gradient(135deg, var(--blue-mid) 0%, var(--blue-deep) 55%, var(--blue-mid) 100%);
  }
  .banner-bands {
    position: absolute;
    inset: 0;
    width: 100%;
    height: 100%;
  }
  .brand-name {
    position: absolute;
    left: 0;
    right: 0;
    top: 66px;
    text-align: center;
    font-family: "Montserrat", sans-serif;
    font-weight: 600;
    font-size: 70px;
    line-height: 1;
    letter-spacing: -0.5px;
    color: var(--logo-white);
  }
  .tagline-panel {
    position: absolute;
    left: 29px;
    top: 223px;
    width: 993px;
    height: 154px;
    background: var(--panel-white);
    display: flex;
    align-items: center;
    justify-content: center;
  }
  .tagline {
    font-family: "Montserrat", sans-serif;
    font-weight: 700;
    font-size: 54px;
    line-height: 1.08;
    text-align: center;
    text-transform: uppercase;
    color: var(--ink);
    letter-spacing: 1px;
  }
  .tagline-line { display: block; }
</style>
</head>
<body>
  <main class="canvas">
    <section class="banner" aria-label="Brightwave Briefings email banner">
      <svg class="banner-bands" viewBox="0 0 1040 390" preserveAspectRatio="none" aria-hidden="true">
        <polygon points="-60,390 240,0 330,0 30,390" fill="var(--band-tint)"/>
        <polygon points="120,390 420,0 470,0 170,390" fill="var(--band-tint)"/>
        <polygon points="560,390 860,0 960,0 660,390" fill="var(--band-tint)"/>
        <polygon points="760,390 1060,0 1100,0 800,390" fill="var(--band-tint)"/>
        <rect x="740" y="-80" width="170" height="150" rx="60" fill="var(--band-accent)" opacity="0.8"/>
        <polygon points="0,390 90,390 140,330 50,330" fill="var(--blue-light)" opacity="0.5"/>
      </svg>
      <h1 class="brand-name">Brightwave Briefings</h1>
      <div class="tagline-panel">
        <p class="tagline">
          <span class="tagline-line">The Systems Expert’s</span>
          <span class="tagline-line">Insight Desk</span>
        </p>
      </div>
    </section>
  </main>
</body>
</html>
```